a board game needs a good card design (5 cards in the same design)

We need a redesign for our cards.
Each card file is 63*88mm, 3mm bleeds - 69mm*94mm, should be done vector and CMYK, because it will be printed.

The game includes 108 cards (don't worry, no needs to design them all), it has:
numbers from 1 to 20 on the yellow background
from 6 to 20 on the green background
+1, +2, +3, +4, +5 on the white background with our logo,
special card on blue background (now it's "+", but it's not necessary, it could be anything with positive meaning, because it's kind of joker card)
circle on red background. We don't want see this circle anymore, it should be replaced to something else. It's the worst card, so the player who draws should understand "oops, that's not good!".

What we need:
now cards look boring and simple, it should look funnier, people hold them and know it's a fun game.
We expect in return 5 cards:
1) any number on the green background
2) any number on the yellow bg.
3) +5 on the white bg with our logo. The white card means the next person should draw cards, so we're fine with our logo on the background, but if you can make up something more interesting, would be great.
4) something on the red bg, what means danger, for a card which could be hard to get rid of
5) something positive on the blue bg, what means you have 2 turns instead of 1, can play this card on any card and place any card on top of it (could sound complicated, just know it's a good card to have)

I've written "color of the background", but these colors are not necessary to come from the background, just overall color of the card should have these primary colors.

All cards should have a big number or whatever in the center and small copies in 2 corners as on standard cards.

Would be great to not make your own font for digits, because we should be able to copy the design to all numbers used.

I have uploaded our logo and current basic design of our cards.

Target Market(s)

the game is suitable for meetup with friends or family play. So it could be anyone from 7 years old to 99

Font styles to use
Sans Serif

Colors
0792cd
ec1f27
fbed22
ffffff
9bcb3b

Requirements
Must have
• the cards must have a number or symbol in the center and on 2 corners (upside down on the bottom corner). Each card must have primary color.
Nice to have
• something on the background, not just color-background. Please use the logo for the background for the white card only.
Should not have
• words, animals, flowers etc
• symbols and digits only please.

```html
<!DOCTYPE html>
<html lang="en">
<head>
<meta charset="utf-8">
<title>Joker Card – Blue</title>
<style>
  :root {
    --card-blue: #3884f8;
    --card-white: #ffffff;
    --page-bg: #ffffff;
  }
  html, body {
    margin: 0;
    padding: 0;
    width: 859px;
    height: 1200px;
    overflow: hidden;
    background: var(--page-bg);
  }
  .card {
    display: block;
    width: 859px;
    height: 1200px;
  }
  .card__face { fill: var(--card-blue); }
  .card__oval { fill: var(--card-white); }
  .card__symbol--center { fill: var(--card-blue); }
  .card__symbol--corner { fill: var(--card-white); }
</style>
</head>
<body>
  <svg class="card" viewBox="0 0 335 468" xmlns="http://www.w3.org/2000/svg" role="img" aria-label="Blue joker card with a large asterisk symbol">
    <defs>
      <g id="asterisk">
        <polygon points="165,232 85,214 85,246"/>
        <polygon points="165,232 245,214 245,246"/>
        <polygon points="165,232 110,162 136,150"/>
        <polygon points="165,232 192,150 219,163"/>
        <polygon points="165,232 108,297 134,309"/>
        <polygon points="165,232 192,310 218,297"/>
      </g>
    </defs>

    <rect class="card__face" x="0" y="0" width="335" height="468" rx="14" ry="14"/>
    <ellipse class="card__oval" cx="167" cy="238" rx="136" ry="200"/>

    <use class="card__symbol--center" href="#asterisk"/>

    <use class="card__symbol--corner" href="#asterisk"
         transform="translate(31 35) scale(0.2) translate(-165 -232)"/>
    <use class="card__symbol--corner" href="#asterisk"
         transform="translate(311 436) rotate(180) scale(0.2) translate(-165 -232)"/>
  </svg>
</body>
</html>
```